Life Coaching business needs a new flyer

We are an Australian business that specialises in Life Coaching, Career Coaching, Health and Wellness Coaching, Yoga and Pilates. We need a A4 double sided flyer that is full colour and folded to DL format. I have attached a couple of designs that I like and some pictures and would like the flyer to be bright yet stylish.

Life Coaching

```html
<!DOCTYPE html>
<html lang="en">
<head>
<meta charset="utf-8">
<title>Clearpath Coaching Studio – Flyer</title>
<link rel="stylesheet" href="https://fonts.googleapis.com/css2?family=Roboto+Condensed:wght@400;700&family=Roboto:wght@400;500;700&display=swap">
<style>
  :root {
    --panel-blue: #5aa5dc;
    --band-blue: #3f9bd0;
    --brand-blue: #2a8ccf;
    --leaf-green: #5bb346;
    --ink: #1f1f1f;
    --ink-navy: #1b3a63;
    --paper: #ffffff;
    --backdrop: #dcdcdc;
  }
  * { margin: 0; padding: 0; box-sizing: border-box; }
  html, body { width: 1200px; height: 1200px; overflow: hidden; }
  body { background: var(--backdrop); position: relative; }

  .flyer {
    position: absolute; left: 80px; top: 232px;
    width: 1300px; height: 918px;
    transform: scale(0.8); transform-origin: 0 0;
    background: var(--paper);
    box-shadow: 0 4px 14px rgba(0,0,0,.25);
    overflow: hidden;
  }
  .flyer__art { position: absolute; inset: 0; }

  .testimonials {
    position: absolute; left: 27px; top: 11px; width: 380px;
    font-family: "Roboto Condensed", sans-serif; font-size: 14px;
    letter-spacing: -0.2px; line-height: 20.2px; color: var(--ink);
  }
  .testimonials__title {
    font-family: "Roboto", sans-serif; font-weight: 700; font-size: 18.5px;
    letter-spacing: 0; text-align: center; margin-bottom: 10px;
  }
  .testimonial { text-align: justify; margin-bottom: 7px; }
  .testimonial b { font-weight: 700; }

  .brand-name {
    position: absolute; font-family: "Roboto Condensed", sans-serif;
    font-weight: 400; color: var(--brand-blue); white-space: nowrap;
  }
  .brand-name--hero { left: 953px; top: 158px; font-size: 38px; }
  .brand-name--intro { left: 446px; top: 552px; font-size: 30px; }

  .services {
    position: absolute; right: 13px; top: 220px; text-align: right;
    font-family: "Roboto", sans-serif; font-size: 20px; line-height: 27px;
    color: var(--ink);
  }

  .intro {
    position: absolute; left: 446px; top: 604px; width: 305px;
    font-family: "Roboto Condensed", sans-serif; font-size: 14px;
    letter-spacing: -0.2px; line-height: 21.5px; color: var(--ink);
  }
  .intro p { margin-bottom: 1px; }
  .contact { margin-top: 2px; font-size: 17px; line-height: 28.5px; letter-spacing: 0; }

  .offer-band {
    position: absolute; left: 433px; top: 827px; width: 402px; height: 91px;
    background: var(--band-blue); padding: 6px 0 0 13px;
    font-family: "Roboto Condensed", sans-serif; font-weight: 700;
    font-size: 19px; line-height: 27px; color: var(--ink-navy);
  }
</style>
</head>
<body>
<main class="flyer">
  <svg class="flyer__art" width="1300" height="918" viewBox="0 0 1300 918">
    <defs>
      <clipPath id="clip-left"><rect x="0" y="0" width="433" height="918"/></clipPath>
      <clipPath id="clip-right"><rect x="433" y="0" width="867" height="918"/></clipPath>
      <linearGradient id="g-friends" x1="0" y1="0" x2="1" y2="1">
        <stop offset="0" stop-color="#c9a27c"/><stop offset="0.5" stop-color="#b84b3e"/><stop offset="1" stop-color="#4b6f99"/>
      </linearGradient>
      <linearGradient id="g-couple" x1="0" y1="0" x2="1" y2="1">
        <stop offset="0" stop-color="#8a7a68"/><stop offset="0.5" stop-color="#3a2c26"/><stop offset="1" stop-color="#6f88a6"/>
      </linearGradient>
      <linearGradient id="g-meditate" x1="0" y1="0" x2="0" y2="1">
        <stop offset="0" stop-color="#8fb6d9"/><stop offset="0.55" stop-color="#c5c8e6"/><stop offset="1" stop-color="#6f9a4a"/>
      </linearGradient>
      <linearGradient id="g-beach" x1="0" y1="0" x2="0" y2="1">
        <stop offset="0" stop-color="#c9e2ef"/><stop offset="1" stop-color="#eef4f7"/>
      </linearGradient>
      <linearGradient id="g-signpost" x1="0" y1="0" x2="0" y2="1">
        <stop offset="0" stop-color="#2f73c4"/><stop offset="0.65" stop-color="#5d9ad8"/><stop offset="1" stop-color="#d9e6f2"/>
      </linearGradient>
    </defs>

    <rect x="0" y="0" width="433" height="918" fill="var(--panel-blue)"/>

    <g clip-path="url(#clip-left)">
      <circle cx="135" cy="800" r="275" fill="var(--leaf-green)"/>
      <circle cx="120" cy="810" r="262" fill="url(#g-friends)" role="img" aria-label="Photo of a group of smiling friends outdoors at sunset"/>
    </g>

    <g clip-path="url(#clip-right)">
      <circle cx="645" cy="165" r="250" fill="var(--leaf-green)"/>
      <circle cx="630" cy="150" r="240" fill="url(#g-couple)" role="img" aria-label="Portrait photo of the two coaches"/>

      <circle cx="1150" cy="760" r="390" fill="var(--leaf-green)"/>
      <circle cx="1160" cy="790" r="390" fill="url(#g-signpost)" role="img" aria-label="Photo of a signpost pointing to life, balance, family, career, health and friends"/>

      <circle cx="960" cy="346" r="93" fill="#1d2430"/>
      <circle cx="962" cy="349" r="88" fill="url(#g-meditate)" role="img" aria-label="Photo of women meditating on mats by the water"/>

      <circle cx="790" cy="467" r="82" fill="#1d2430"/>
      <circle cx="792" cy="470" r="78" fill="url(#g-beach)" role="img" aria-label="Photo of a couple doing a yoga tree pose on the beach"/>
    </g>
  </svg>

  <section class="testimonials">
    <h2 class="testimonials__title">Happy Clients Testimonials</h2>
    <p class="testimonial">“I have lost 10 kilos and now have the energy to play with my kids. Thanks Tessa for you support/guidance and helping me get rid of my limiting beliefs. I feel I can achieve anything now! The sky’s the limit” - <b>Leah, Mosman</b></p>
    <p class="testimonial">“I had always wanted to start up own café however every time it came to putting it into practice I would procrastinate and not achieve anything. I became overwhelmed with the whole process and never achieved anything. Tessa put it into bite sized chunks and helped me to set small achievable goals. I am now a happy café owner.” - <b>Nora, Double Bay</b></p>
    <p class="testimonial">“Tessa has helped to change my life around in all aspects. I would have been lost without her. Thanks Tessa for your professionalism, support and guidance.” - <b>Beth, Cremorne</b></p>
    <p class="testimonial">“I was so busy with kids, work, and my husband I lost who I was. Tessa has helped me find the person I am again.” <b>Sophie, Chatswood</b></p>
    <p class="testimonial">“When I started with Coach Tessa, I didn’t know anything about coaching. I called her because she helped a friend of mine make a career change that was a perfect fit for her. I had the opportunity to make a change too and did not know where to start. I am now in a job that I love. I would recommend Tessa to everyone.” <b>Jacob, Texas America</b></p>
  </section>

  <div class="brand-name brand-name--hero">Clearpath Coaching</div>
  <div class="services">Life Coaching<br>Meditation<br>Yoga/Pilates.</div>

  <div class="brand-name brand-name--intro">Clearpath Coaching</div>
  <section class="intro">
    <p>Clearpath Coaching Studio is a professional service that can help you achieve the goals that you are looking for in <b>Life Coaching, Meditation, and Yoga/Pilates.</b></p>
    <p>If you are ready to take your life to the next level and would like to know more, please contact us.</p>
    <div class="contact">
      Phone: 02 9000 4127<br>
      Email:hello@clearpathcoaching.com.au<br>
      www.clearpathcoaching.com.au
    </div>
  </section>

  <div class="offer-band">
    Free Introductory Life Coaching<br>
    Phone/Video session - 20 mins<br>
    (To see if coaching is right for you)
  </div>
</main>
</body>
</html>
```